Join Our Real Estate Team

I would like to purchase a customized version of a design you have previously submitted - https://www.plumvexa.com/design/61937042

I want to create a recruitment AD. I have attached a AD I have created and would like as much of this information on an AD as possible. My main GOAL is to promote $350 Flat Fee (Includes E&O) per Transaction & No Monthly Fees.
I like to use a photo stock as I have in the attachment of various people.
I DON'T want to say "Wanted". Prefer to say something like "STOP Paying High Splits...Keep Most of YOUR hard earned Commissions"
Feel free to use other formats that might fit all the information that I have in my flyer I have uploaded.

Target Market(s)

Realtors

Industry/Entity Type

Real Estate

Font styles to use
Serif

Colors
0094D4
00A9DD
6FCCEA
C7EBF8
E9F6FB

Requirements
Must have
• See uploaded flyer to get must haves
Nice to have
• See uploaded flyer to get ideas
Should not have
• Do not want it to say "wanted"

```html
<!DOCTYPE html>
<html lang="en">
<head>
<meta charset="utf-8">
<title>Join Our Team – Flat Fee Recruitment Flyer</title>
<link href="https://fonts.googleapis.com/css2?family=Oswald:wght@500;700&family=Montserrat:wght@400;500;600;700;800;900&display=swap" rel="stylesheet">
<style>
  :root{
    --forest:#03352b;
    --teal:#5ccfd6;
    --teal-soft:#80d6dc;
    --teal-pale:#d5f6f7;
    --ink:#141414;
    --slate:#4d4d4d;
    --white:#ffffff;
  }
  *{margin:0;padding:0;box-sizing:border-box}
  html,body{width:750px;height:1200px;overflow:hidden;background:var(--white)}
  .flyer{position:relative;width:750px;height:1200px;overflow:hidden;background:var(--white);font-family:'Montserrat',sans-serif;color:var(--ink)}
  .abs{position:absolute}
  .condensed{font-family:'Oswald',sans-serif}

  .hero-art{position:absolute;left:0;top:0}
  .brand{left:40px;top:64px;width:220px;text-align:center}
  .brand-mark{width:26px;height:26px;border-radius:50%;background:var(--teal);margin:0 auto 12px}
  .brand-name{font-weight:700;font-size:19px;color:var(--forest);letter-spacing:.3px;line-height:1.1;white-space:nowrap}
  .brand-sub{font-weight:600;font-size:9px;color:var(--forest);letter-spacing:2px;margin-top:4px;white-space:nowrap}
  .license{right:36px;top:44px;text-align:right;font-weight:700;font-size:14px;line-height:1.35;color:var(--ink)}

  .price{left:44px;top:212px;font-size:92px;font-weight:700;color:var(--white);line-height:1;letter-spacing:-1px}
  .price sup{font-size:40px;vertical-align:top;position:relative;top:8px}
  .price .star{font-size:52px;vertical-align:top}
  .flat-fee{left:46px;top:330px;font-weight:900;font-size:46px;line-height:1;letter-spacing:-.5px}
  .includes{left:46px;top:378px;font-size:22px;font-weight:500}
  .includes b{font-weight:800}

  .example{left:48px;top:492px;width:259px;height:342px;background:var(--forest);color:var(--white);text-align:center}
  .example .on-a{margin-top:40px;font-family:'Montserrat',sans-serif;font-weight:600;font-size:16px;display:flex;align-items:center;justify-content:center;gap:8px}
  .example .on-a::before,.example .on-a::after{content:"";width:54px;height:1px;background:var(--white)}
  .example .sale{font-size:38px;font-weight:500;line-height:1.1;margin-top:6px;letter-spacing:-.5px}
  .example .sale sup{font-size:18px}
  .example .rate{font-size:33px;font-weight:500;line-height:1.1;letter-spacing:-.5px}
  .result-band{left:42px;top:677px;width:271px;height:43px;background:var(--teal-soft);color:var(--forest);font-size:27px;font-weight:500;text-align:center;line-height:43px;letter-spacing:-.5px}
  .result-band sup{font-size:14px}
  .earned{left:48px;top:745px;width:259px;text-align:center;color:var(--white);font-size:15px;line-height:1.55}
  .earned b{font-weight:700;font-size:21px}

  .join{left:48px;top:855px;width:259px;text-align:center;font-size:32px;letter-spacing:-.5px;white-space:nowrap}
  .join .light{font-weight:400;color:var(--teal)}
  .join .bold{font-weight:800;color:var(--forest)}
  .join-dash{left:162px;top:912px;width:32px;height:4px;background:var(--forest)}
  .earn-box{left:48px;top:918px;width:259px;height:97px;border:1px solid var(--teal);text-align:center;padding-top:16px;line-height:1.05}
  .earn-box .l1{font-size:27px;font-weight:500;color:var(--ink)}
  .earn-box .l2{font-size:29px;font-weight:800}
  .earn-box .l2 .t{color:var(--teal)}
  .earn-box .l2 .d{color:var(--forest)}

  .per-tx{left:342px;top:482px;font-size:46px;font-weight:700;color:var(--teal);white-space:nowrap;line-height:1.1;transform:scaleY(1.28);transform-origin:left top}
  .perks{left:344px;top:555px;display:flex;gap:28px;font-weight:600;font-size:17px}
  .perk{display:flex;align-items:center;gap:6px}
  .stop{left:343px;top:614px;font-weight:800;font-size:29px;line-height:1.1;color:var(--forest)}
  .stop .thin{font-weight:500;color:var(--slate)}
  .stop-divider{left:556px;top:618px;width:0;height:56px;border-left:2px dotted var(--slate)}
  .keep{left:571px;top:615px;font-size:15.5px;line-height:1.45;color:var(--slate)}

  .office-photo{left:339px;top:705px;width:366px;height:184px}
  .frustrated{left:339px;top:887px;width:218px;height:77px;background:var(--slate);color:var(--white);padding:10px 0 0 26px;line-height:1.05}
  .frustrated .q{font-size:24px;font-weight:500}
  .frustrated .w{font-size:30px;font-weight:800}
  .giving{left:557px;top:887px;width:148px;height:77px;background:var(--teal-pale);padding:14px 0 0 13px;font-size:12.5px;line-height:1.4;color:var(--ink)}
  .giving b{font-weight:800}
  .tagline{left:339px;top:985px;font-size:27px;font-weight:500;color:var(--ink);white-space:nowrap}
  .tagline b{font-weight:800}

  .footer-band{left:0;top:1085px;width:750px;height:115px;background:var(--teal-soft)}
  .phone-pill{left:229px;top:1058px;width:290px;height:48px;border-radius:24px;background:var(--forest);border:3px solid var(--white);box-shadow:0 0 0 1px var(--forest);color:var(--white);display:flex;align-items:center;justify-content:center;gap:8px;font-weight:700;font-size:28px}
  .avatar{left:48px;top:1113px;width:64px;height:64px;border-radius:50%;background:radial-gradient(circle at 50% 40%,#e9d7c8,#9a8171);border:3px solid var(--white)}
  .agent-name{left:121px;top:1126px;font-weight:800;font-size:36px;color:var(--white);letter-spacing:-.5px;white-space:nowrap}
  .contact-divider{left:404px;top:1122px;height:60px;border-left:2px dotted var(--forest)}
  .contacts{left:420px;top:1128px;font-weight:600;font-size:14px;line-height:1.55;color:var(--forest);white-space:nowrap}
  .contacts div{display:flex;align-items:center;gap:6px}
</style>
</head>
<body>
<main class="flyer">

  <svg class="hero-art" width="750" height="440" viewBox="0 0 750 440">
    <defs>
      <linearGradient id="officeTone" x1="0" y1="0" x2="1" y2="1">
        <stop offset="0" stop-color="#a9e6ea"/>
        <stop offset=".55" stop-color="#5fc7cd"/>
        <stop offset="1" stop-color="#3a4a48"/>
      </linearGradient>
    </defs>
    <polygon role="img" aria-label="Photo of real estate agents meeting around an office table"
      points="250,204 367,41 459,157 538,39 627,134 750,86 750,435 250,435" fill="url(#officeTone)"/>
    <polygon points="0,207 407,207 323,323 0,323" fill="var(--forest)"/>
    <polygon points="0,323 323,323 266,414 0,414" fill="var(--white)"/>
    <line x1="440" y1="166" x2="283" y2="414" stroke="var(--white)" stroke-width="10"/>
    <line x1="455" y1="170" x2="300" y2="414" stroke="var(--teal)" stroke-width="4"/>
    <rect x="0" y="414" width="750" height="21" fill="var(--teal-soft)"/>
  </svg>

  <div class="abs brand">
    <div class="brand-mark"></div>
    <div class="brand-name">COASTAL HARBOR</div>
    <div class="brand-sub">REALTY GROUP, LLC</div>
  </div>
  <div class="abs license">BK 4471902<br>CQ 2093618</div>

  <div class="abs price condensed"><sup>$</sup>350<span class="star">*</span></div>
  <div class="abs flat-fee">FLAT FEE</div>
  <div class="abs includes">includes <b>E</b> and <b>O</b></div>

  <section class="abs example condensed">
    <div class="on-a">ON A</div>
    <div class="sale"><sup>$</sup>250,000 SALE</div>
    <div class="rate">W/3% COMMISION</div>
  </section>
  <div class="abs result-band condensed"><sup>$</sup>350* FLAT FEE= <sup>$</sup>7150</div>
  <div class="abs earned">Commission Earned<br><b>w/CHRG</b></div>

  <div class="abs join"><span class="light">JOIN </span><span class="bold">OUR TEAM</span></div>
  <div class="abs join-dash"></div>
  <div class="abs earn-box">
    <div class="l1">START EARNING</div>
    <div class="l2"><span class="t">MORE </span><span class="d">TODAY</span></div>
  </div>

  <div class="abs per-tx condensed">PER TRANSACTION</div>
  <div class="abs perks">
    <span class="perk"><svg width="17" height="17" viewBox="0 0 17 17"><circle cx="8.5" cy="8.5" r="8.5" fill="#20a8c8"/><path d="M4.5 8.8l2.7 2.6 5.3-5.4" stroke="#fff" stroke-width="2" fill="none"/></svg>No monthly fees</span>
    <span class="perk"><svg width="17" height="17" viewBox="0 0 17 17"><circle cx="8.5" cy="8.5" r="8.5" fill="#20a8c8"/><path d="M4.5 8.8l2.7 2.6 5.3-5.4" stroke="#fff" stroke-width="2" fill="none"/></svg>Timely payouts</span>
  </div>
  <div class="abs stop"><span class="thin">STOP PAYING</span><br>HIGH SPIRITS</div>
  <div class="abs stop-divider"></div>
  <div class="abs keep">Keep most of<br>your hard earned<br>commissions</div>

  <div class="abs office-photo" role="img" aria-label="Photo of a stressed agent on the phone at a desk with a computer and lamp"
       style="background:linear-gradient(90deg,#e4e6e8 0%,#f4f4f4 45%,#dcdcdc 100%)"></div>
  <div class="abs frustrated"><div class="q">Are you</div><div class="w">Frustrated</div></div>
  <div class="abs giving">giving up <b>20%, 30%</b><br>or even <b>50%</b> of your<br>Commission ???</div>
  <div class="abs tagline">Your “<b>fen</b>” Nomenal Broker</div>

  <div class="abs footer-band"></div>
  <div class="abs phone-pill">
    <svg width="20" height="20" viewBox="0 0 24 24"><path d="M6.6 10.8c1.4 2.8 3.8 5.1 6.6 6.6l2.2-2.2c.3-.3.7-.4 1-.2 1.1.4 2.3.6 3.6.6.6 0 1 .4 1 1V20c0 .6-.4 1-1 1C10.6 21 3 13.4 3 4c0-.6.4-1 1-1h3.5c.6 0 1 .4 1 1 0 1.3.2 2.5.6 3.6.1.3 0 .7-.2 1L6.6 10.8z" fill="none" stroke="#fff" stroke-width="1.6"/></svg>
    555.310.4872
  </div>
  <div class="abs avatar" role="img" aria-label="Portrait photo of the broker"></div>
  <div class="abs agent-name">FEN MARLOW</div>
  <div class="abs contact-divider"></div>
  <div class="abs contacts">
    <div><svg width="11" height="8" viewBox="0 0 11 8"><rect x=".5" y=".5" width="10" height="7" fill="none" stroke="#fff"/><path d="M.5 .5l5 4 5-4" stroke="#fff" fill="none"/></svg>fen@CHrealtyGRP.com</div>
    <div><svg width="11" height="11" viewBox="0 0 11 11"><circle cx="5.5" cy="5.5" r="5" fill="none" stroke="#fff"/><path d="M.5 5.5h10M5.5 .5c-2.5 3-2.5 7 0 10M5.5 .5c2.5 3 2.5 7 0 10" stroke="#fff" fill="none"/></svg>www.coastalharborrealtygroup.com</div>
  </div>

</main>
</body>
</html>
```